Business card design only (Have Logo Online) Shoudl be quick and easy for designer

We would like to have a business card design that is in-line with our company logo. Final deliverables should include two EPS extension file. One for the front card design and the other the back-end design. Please also indicate the font style used.

Advisory Pebbles is a social enterprise that focuses on utilizing technology, unique methodologies and international partnerships to provide a one-stop location for economical and dependable IT-related solutions.

Target Market(s)

Micro, small and medium business owners.

Industry/Entity Type

Business

Requirements
Must have
• The business card should incorporate our company logo.
Nice to have
• A little web 2.0 style would be nice but I haven''t decided yet.

```html
<!DOCTYPE html>
<html lang="en">
<head>
<meta charset="utf-8">
<title>Advisory Pebbles – Business Card</title>
<link rel="stylesheet" href="https://fonts.googleapis.com/css2?family=Open+Sans:ital,wght@0,400;0,700;1,700&display=swap">
<style>
  :root {
    --page-bg: #ffffff;
    --brand-green: #3f8a4a;
    --card-green: #559b60;
    --soft-green: #b9dba2;
    --faint-white: rgba(255, 255, 255, 0.13);
    --ink: #222222;
    --card-border: #c9c9c9;
    --white: #ffffff;
  }
  * { margin: 0; padding: 0; box-sizing: border-box; }
  html, body { width: 1200px; height: 901px; overflow: hidden; background: var(--page-bg); }
  body { font-family: "Open Sans", Verdana, sans-serif; position: relative; color: var(--ink); }

  .brand-lockup { position: absolute; display: flex; align-items: center; }
  .brand-mark { border-radius: 50%; flex: none; }
  .brand-name {
    font-family: "Open Sans", Verdana, sans-serif;
    font-weight: 700;
    text-transform: uppercase;
    letter-spacing: 0.02em;
    white-space: nowrap;
  }

  /* standalone logo presentation */
  .brand-lockup--showcase { left: 175px; top: 150px; gap: 22px; }
  .brand-lockup--showcase .brand-mark { width: 190px; height: 190px; background: var(--soft-green); }
  .brand-lockup--showcase .brand-name { font-size: 36px; color: var(--brand-green); }

  /* back of card */
  .card-back {
    position: absolute; left: 26px; top: 454px; width: 733px; height: 418px;
    background: var(--card-green); overflow: hidden;
  }
  .card-back__accent {
    position: absolute; left: 330px; top: 0px; width: 520px; height: 520px;
    border-radius: 50%; border: 70px solid var(--faint-white);
  }
  .card-back .brand-lockup { left: 28px; top: 176px; gap: 20px; }
  .card-back .brand-mark { width: 204px; height: 204px; border: 14px solid var(--white); }
  .card-back .brand-name { font-size: 32px; color: var(--white); }

  /* front of card */
  .card-front {
    position: absolute; left: 766px; top: 134px; width: 426px; height: 738px;
    background: var(--white); border: 2px solid var(--card-border); overflow: hidden;
  }
  .card-front .brand-lockup { left: 38px; top: 82px; gap: 16px; }
  .card-front .brand-mark { width: 146px; height: 146px; background: var(--soft-green); }
  .card-front .brand-name { font-size: 19px; color: var(--brand-green); }

  .contact { position: absolute; left: 50px; top: 432px; letter-spacing: 0.1em; }
  .contact__name { font-size: 22px; font-weight: 700; font-style: italic; color: var(--ink); }
  .contact__title { font-size: 16px; margin-top: 10px; }
  .contact__lines { list-style: none; margin-top: 54px; font-size: 16px; line-height: 38px; }
</style>
</head>
<body>
  <div class="brand-lockup brand-lockup--showcase">
    <span class="brand-mark"></span>
    <span class="brand-name">Advisory Pebbles</span>
  </div>

  <section class="card-back" aria-label="Business card back">
    <span class="card-back__accent"></span>
    <div class="brand-lockup">
      <span class="brand-mark"></span>
      <span class="brand-name">Advisory Pebbles</span>
    </div>
  </section>

  <section class="card-front" aria-label="Business card front">
    <div class="brand-lockup">
      <span class="brand-mark"></span>
      <span class="brand-name">Advisory Pebbles</span>
    </div>
    <div class="contact">
      <p class="contact__name">Your Name</p>
      <p class="contact__title">Job Title</p>
      <ul class="contact__lines">
        <li>p (555) 555-5555</li>
        <li>f (555) 555-5555</li>
        <li>yourname@advisorypebbles.com</li>
      </ul>
    </div>
  </section>
</body>
</html>
```